Brochure Design Project

We need a brochure designed for our company, specifically targeted at our corporate business customers ... Banks, Financial Services, Government. The brochure needs to detail our services and what we have to offer.

It may be a brochure/booklet that we can give to clients when we meet them. It needs to have a very corporate look and feel and needs to align with our colour palette and logo.

Information is held on our website www.tessaroworldservices.com
Updates

Thank you everyone for being part of this project.  It was a very hard decision.

Target Market(s)

Corporate business and clients including banks, financial services, insurance and government.

Industry/Entity Type

Business

Requirements
Must have
• Must have a corporate and global feel to it.
Must have our logo and same or similar colour palette.

```html
<!DOCTYPE html>
<html lang="en">
<head>
<meta charset="utf-8">
<title>Tessaro World Services – Corporate Brochure</title>
<link rel="stylesheet" href="https://fonts.googleapis.com/css2?family=PT+Sans:wght@400;700&display=swap">
<style>
  :root {
    --stage: #4a4a4a;
    --stage-light: #6a6a6a;
    --paper: #ffffff;
    --brand-blue: #1d4f9c;
    --brand-blue-mid: #3b78c4;
    --sky-top: #17418c;
    --sky-mid: #4f86cf;
    --sky-low: #b9d3ef;
    --swoosh-grey: #a3a6ab;
    --ink-dark: #222222;
    --accent-green: #8dc63f;
    --rule-light: rgba(255,255,255,0.55);
  }
  * { box-sizing: border-box; margin: 0; padding: 0; }
  html, body { width: 1200px; height: 753px; overflow: hidden; }
  body {
    font-family: "PT Sans", Arial, sans-serif;
    background: radial-gradient(ellipse at 50% 40%, var(--stage-light), var(--stage) 75%);
  }
  .canvas { position: relative; width: 1200px; height: 753px; }

  .panel {
    position: absolute;
    top: 116px;
    width: 520px;
    height: 520px;
    background: var(--paper);
    overflow: hidden;
    box-shadow: 0 10px 30px rgba(0,0,0,0.35);
  }
  .panel--front { left: 60px; border-bottom: 4px solid var(--accent-green); }
  .panel--back { left: 620px; }
  .panel svg.shapes { position: absolute; inset: 0; }

  /* Front cover */
  .cover-title {
    position: absolute;
    top: 34px;
    right: 34px;
    color: var(--paper);
    text-align: left;
  }
  .cover-title__main { font-size: 44px; font-weight: 400; line-height: 1; letter-spacing: 0.5px; }
  .cover-title__sub { font-size: 17px; line-height: 1.2; margin-top: 6px; }

  .brand-lockup {
    position: absolute;
    top: 312px;
    left: 356px;
    display: flex;
    align-items: center;
    gap: 8px;
  }
  .brand-lockup__dot {
    width: 28px; height: 28px; border-radius: 50%;
    background: var(--brand-blue);
  }
  .brand-lockup__name {
    font-size: 17px; font-weight: 700; color: var(--brand-blue);
    letter-spacing: 0.5px;
  }
  .cover-url {
    position: absolute;
    left: 30px;
    bottom: 26px;
    font-size: 18px;
    font-weight: 700;
    color: var(--brand-blue);
  }

  /* Back cover */
  .back-copy {
    position: absolute;
    top: 96px;
    left: 160px;
    width: 320px;
    color: var(--paper);
    font-size: 12px;
    line-height: 1.45;
  }
  .back-copy p + p { margin-top: 9px; }
  .contact {
    position: absolute;
    top: 228px;
    left: 160px;
    width: 320px;
    color: var(--paper);
    font-size: 12.5px;
    line-height: 1.4;
  }
  .contact__company { font-weight: 700; font-size: 13.5px; }
  .contact__address { margin-bottom: 22px; }
  .back-brand {
    position: absolute;
    left: 0; right: 0;
    bottom: 30px;
    display: flex;
    justify-content: center;
    align-items: center;
    gap: 6px;
  }
  .back-brand .brand-lockup__dot { width: 16px; height: 16px; }
  .back-brand .brand-lockup__name { font-size: 12px; }
</style>
</head>
<body>
<div class="canvas">

  <!-- Front cover -->
  <section class="panel panel--front">
    <svg class="shapes" width="520" height="520" viewBox="0 0 520 520" aria-hidden="true">
      <defs>
        <linearGradient id="skyFill" x1="0" y1="0" x2="0" y2="1">
          <stop offset="0" stop-color="var(--sky-top)"/>
          <stop offset="0.55" stop-color="var(--sky-mid)"/>
          <stop offset="1" stop-color="var(--sky-low)"/>
        </linearGradient>
        <linearGradient id="roundFill" x1="0" y1="0" x2="1" y2="1">
          <stop offset="0" stop-color="#7fb0e6"/>
          <stop offset="1" stop-color="#2b5fae"/>
        </linearGradient>
      </defs>
      <path d="M0,395 C220,380 420,310 520,200" fill="none" stroke="var(--swoosh-grey)" stroke-width="7"/>
    </svg>
    <svg class="shapes" width="520" height="520" viewBox="0 0 520 520" role="img" aria-label="Photograph: empty boardroom chairs around a long white table under a blue sky with clouds">
      <path d="M0,0 H520 V188 C420,300 220,368 0,384 Z" fill="url(#skyFill)"/>
    </svg>
    <svg class="shapes" width="520" height="520" viewBox="0 0 520 520" role="img" aria-label="Round photograph: business handshake">
      <circle cx="150" cy="398" r="44" fill="url(#roundFill)" stroke="var(--ink-dark)" stroke-width="6"/>
    </svg>

    <div class="cover-title">
      <h1 class="cover-title__main">Specialists in</h1>
      <p class="cover-title__sub">Transformational Change &amp;<br>Sustainable Solutions</p>
    </div>

    <div class="brand-lockup">
      <span class="brand-lockup__dot"></span>
      <span class="brand-lockup__name">TESSARO</span>
    </div>

    <p class="cover-url">www.tessaroworldservices.com</p>
  </section>

  <!-- Back cover -->
  <section class="panel panel--back">
    <svg class="shapes" width="520" height="520" viewBox="0 0 520 520" aria-hidden="true">
      <path d="M0,0 H520 V372 C400,392 210,418 0,436 Z" fill="var(--brand-blue-mid)"/>
      <path d="M0,446 C210,428 400,402 520,382" fill="none" stroke="var(--swoosh-grey)" stroke-width="7"/>
      <circle cx="318" cy="42" r="18" fill="none" stroke="rgba(255,255,255,0.3)" stroke-width="1.5"/>
      <line x1="140" y1="0" x2="140" y2="380" stroke="var(--rule-light)" stroke-width="1"/>
      <line x1="140" y1="80" x2="490" y2="80" stroke="var(--rule-light)" stroke-width="1"/>
      <line x1="140" y1="214" x2="490" y2="214" stroke="var(--rule-light)" stroke-width="1"/>
    </svg>

    <div class="back-copy">
      <p>Tessaro is the partner organisations call upon when they need a team that can cut through complex problems quickly and efficiently, even in cases that seem intractable.</p>
      <p>Whether you face growth, risk or change, TWS can help:</p>
      <p>We bring a clear view of how to bring it all together, managing all the moving parts.</p>
    </div>

    <div class="contact">
      <p class="contact__company">Tessaro World Services Pty Ltd</p>
      <p class="contact__address">Harbour Lane West<br>Docklands VIC 3008<br>AUSTRALIA</p>
      <p>+61 (03) 9000 4821<br>info@tessaroworldservices.com<br>www.tessaroworldservices.com</p>
    </div>

    <div class="back-brand">
      <span class="brand-lockup__dot"></span>
      <span class="brand-lockup__name">TESSARO</span>
    </div>
  </section>

</div>
</body>
</html>
```